Dorrie's Letterhead

Letterhead should say: Dorrie Fenwick Childern's Book Author/Illustrator

Font should be fun and colorful, but not so distracting that it over shadows the letters content. My business card is shaped like a bone so I would like to keep that shape somewhere in the theme of the letterhead. You can find my book on Bookvale Wiggo and the Silver Kite if you would like to get a sense of my artistic style.
Updates

While I did say I want to carry out the bone theme. Don't be afraid to expand on that example: book shaped like a bone, paint brush...really go for it.

Surprise me! Good luck

Target Market(s)

Adults buying my book

Industry/Entity Type

Business

Requirements
Must have
• Fun colorful
Should not have
• Only one color

```html
<!DOCTYPE html>
<html lang="en">
<head>
<meta charset="UTF-8">
<title>Dorrie Fenwick – Letterhead</title>
<link href="https://fonts.googleapis.com/css2?family=Bangers&family=Lilita+One&display=swap" rel="stylesheet">
<style>
  :root {
    --backdrop: #5b5b5b;
    --paper: #ffffff;
    --doodle-pink: #f6a8bf;
    --doodle-pink-soft: #f9c3d3;
    --doodle-pale: #e6e6e6;
    --subtitle-orange: #f26a21;
    --contact-purple: #7b3fa0;
    --c-navy: #1f3c93;
    --c-blue: #2a7fd1;
    --c-green: #3aa845;
    --c-yellow: #f7d81b;
    --c-orange: #f58a1f;
    --c-red: #e5302b;
    --c-pink: #e53a8c;
    --c-purple: #7a3b9c;
    --c-teal: #1c8a7c;
  }
  * { margin: 0; padding: 0; box-sizing: border-box; }
  html, body {
    width: 1032px;
    height: 1200px;
    overflow: hidden;
    background: var(--backdrop);
  }
  .letterhead {
    position: relative;
    width: 1032px;
    height: 1200px;
  }
  .bone-sheet {
    position: absolute;
    inset: 0;
  }
  .name {
    position: absolute;
    left: 706px;
    top: 374px;
    writing-mode: vertical-rl;
    text-orientation: sideways;
    font-family: "Lilita One", "Arial Black", sans-serif;
    font-weight: 400;
    font-size: 52px;
    letter-spacing: 1px;
    line-height: 1;
    white-space: nowrap;
  }
  .name .c1 { color: var(--c-navy); }
  .name .c2 { color: var(--c-blue); }
  .name .c3 { color: var(--c-green); }
  .name .c4 { color: var(--c-yellow); }
  .name .c5 { color: var(--c-orange); }
  .name .c6 { color: var(--c-red); }
  .name .c7 { color: var(--c-pink); }
  .name .c8 { color: var(--c-purple); }
  .name .c9 { color: var(--c-teal); }
  .role {
    position: absolute;
    left: 654px;
    top: 262px;
    writing-mode: vertical-rl;
    text-orientation: sideways;
    font-family: "Bangers", "Impact", sans-serif;
    font-size: 35px;
    letter-spacing: 5.6px;
    line-height: 1;
    color: var(--subtitle-orange);
    white-space: nowrap;
  }
  .contact {
    position: absolute;
    left: 171px;
    top: 1034px;
    font-family: "Bangers", "Impact", sans-serif;
    font-style: normal;
    font-size: 27px;
    letter-spacing: 4px;
    line-height: 32px;
    color: var(--contact-purple);
    white-space: nowrap;
  }
</style>
</head>
<body>
<main class="letterhead">
  <svg class="bone-sheet" width="1032" height="1200" viewBox="0 0 1032 1200" xmlns="http://www.w3.org/2000/svg">
    <defs>
      <clipPath id="bone-outline">
        <path d="M150 82 H720 C805 82 870 145 870 232 C870 318 812 360 792 380 Q775 398 775 420 V780 Q775 802 792 820 C812 840 870 882 870 968 C870 1055 805 1114 720 1114 H150 Z"/>
      </clipPath>
      <linearGradient id="pale-fade" x1="0" y1="0" x2="1" y2="0">
        <stop offset="0" stop-color="var(--doodle-pale)"/>
        <stop offset="1" stop-color="var(--paper)"/>
      </linearGradient>
      <linearGradient id="pink-fade" x1="0" y1="0" x2="0" y2="1">
        <stop offset="0" stop-color="var(--doodle-pink)"/>
        <stop offset="0.5" stop-color="var(--doodle-pink-soft)"/>
        <stop offset="1" stop-color="var(--doodle-pink)"/>
      </linearGradient>
    </defs>
    <path class="bone-paper" fill="var(--paper)" d="M150 82 H720 C805 82 870 145 870 232 C870 318 812 360 792 380 Q775 398 775 420 V780 Q775 802 792 820 C812 840 870 882 870 968 C870 1055 805 1114 720 1114 H150 Z"/>
    <g class="doodle-art" clip-path="url(#bone-outline)" role="img" aria-label="Pink line-art doodle illustration of playful monsters, rainbows, stars and paint drips along the left edge">
      <path class="doodle-pale-zone" fill="url(#pale-fade)" d="M150 82 H735 C700 150 640 210 600 300 C575 360 570 420 560 480 V860 C600 900 620 1000 610 1114 H150 Z"/>
      <path class="doodle-pink-zone" fill="url(#pink-fade)" d="M150 82 H700 C660 125 610 150 540 165 C450 180 385 220 378 300 V860 C335 880 295 940 282 1114 H150 Z"/>
      <path class="doodle-pink-tip" fill="var(--doodle-pink)" d="M545 1114 Q560 1070 576 1036 Q592 1070 608 1114 Z"/>
    </g>
  </svg>

  <h1 class="name"><span class="c1">D</span><span class="c2">O</span><span class="c3">R</span><span class="c4">R</span><span class="c5">I</span><span class="c6">E</span> <span class="c7">F</span><span class="c8">E</span><span class="c2">N</span><span class="c1">W</span><span class="c9">I</span><span class="c3">C</span><span class="c5">K</span></h1>
  <p class="role">CHILDERN'S BOOK AUTHOR/ILLUSTRATOR</p>

  <address class="contact">
    CELL:(555)210-4873<br>
    EMAIL:DORRIEDRAWS@MAILBOX.NET
  </address>
</main>
</body>
</html>
```